Marrowind Lake Billboard

Looking to design a multi purpose billboard promoting Marrowind Lake as a destination point. Billboard size is 12ft x 40ft
My goal is to advertise our restaurant The Driftmill (pic attached)
What makes Marrowind a destination? It offers lodging / water skiing / Off Road Adventure / Camping / Fishing / Hunting
Want a catch phrase, something like "Looking For a Getaway" or "Need a Break"
Needs to really pop and catch the interest of the looker
maybe have our website address www.marrowinddriftmill.example
Open for ideas

```html
<!DOCTYPE html>
<html lang="en">
<head>
<meta charset="utf-8">
<title>The Driftmill – Marrowind Lake Billboard</title>
<link rel="stylesheet" href="https://fonts.googleapis.com/css2?family=Alfa+Slab+One&family=Rye&family=Bangers&family=Roboto+Slab:wght@500&display=swap">
<style>
  :root {
    --page-bg: #e2e2e2;
    --wood-dark: #2e2119;
    --wood-mid: #4a3628;
    --wood-light: #5b4433;
    --plank-line: rgba(15, 9, 5, 0.55);
    --cream: #f3dfc3;
    --white: #ffffff;
    --slice: #efc79a;
    --slice-ring: #c98a52;
    --frame: #e08a2c;
    --frame-dark: #8a4f1a;
    --ribs-a: #c4531f;
    --ribs-b: #7a2b10;
    --wrap-a: #e9d9b8;
    --wrap-b: #5d8f3a;
  }
  html, body {
    margin: 0;
    width: 1048px;
    height: 1200px;
    overflow: hidden;
    background: var(--page-bg);
  }
  .billboard {
    position: absolute;
    left: 24px;
    top: 450px;
    width: 1000px;
    height: 300px;
    overflow: hidden;
    box-shadow: 0 14px 30px rgba(0, 0, 0, 0.35);
    background:
      repeating-linear-gradient(90deg, transparent 0 54px, var(--plank-line) 54px 56px),
      linear-gradient(90deg, var(--wood-dark), var(--wood-mid) 30%, var(--wood-light) 50%, var(--wood-mid) 70%, var(--wood-dark));
  }
  .food-frame {
    position: absolute;
    width: 160px;
    height: 160px;
    transform: translate(-50%, -50%) rotate(45deg);
    border: 9px solid var(--frame);
    outline: 2px solid var(--frame-dark);
    box-sizing: border-box;
  }
  .food-frame--ribs { left: 138px; top: 134px; background: linear-gradient(45deg, #2a1a12, var(--ribs-a) 35%, var(--ribs-b) 65%, #3a2516); }
  .food-frame--wrap { left: 861px; top: 134px; background: linear-gradient(45deg, var(--wrap-b), var(--wrap-a) 55%, #d9c3a0); }
  .activity-slice {
    position: absolute;
    width: 52px;
    height: 52px;
    border-radius: 50%;
    transform: translate(-50%, -50%);
    background: radial-gradient(circle, var(--slice) 60%, var(--slice-ring) 100%);
    border: 2px solid var(--frame-dark);
    box-sizing: border-box;
  }
  .brand {
    position: absolute;
    left: 501px;
    transform: translateX(-50%);
    color: var(--white);
    text-align: center;
    white-space: nowrap;
    font-family: "Alfa Slab One", serif;
  }
  .brand__the { top: 16px; font-size: 17px; }
  .brand__name { top: 40px; font-size: 38px; letter-spacing: 1px; line-height: 1; }
  .brand__place { top: 86px; font-family: "Roboto Slab", serif; font-weight: 500; font-size: 14px; }
  .tagline {
    position: absolute;
    left: 501px;
    top: 112px;
    transform: translateX(-50%);
    margin: 0;
    font-family: "Rye", serif;
    font-weight: 400;
    font-size: 44px;
    line-height: 1;
    color: var(--cream);
    white-space: nowrap;
  }
  .activities {
    position: absolute;
    margin: 0;
    padding: 0;
    list-style: none;
  }
  .activities--left { left: 299px; top: 183px; }
  .activities--right { left: 587px; top: 183px; }
  .activities li {
    display: flex;
    align-items: center;
    height: 34.5px;
    font-family: "Bangers", sans-serif;
    font-size: 19px;
    letter-spacing: 0.5px;
    color: var(--cream);
  }
  .activities .bullet {
    width: 22px;
    height: 22px;
    border-radius: 50%;
    margin-right: 12px;
    background: radial-gradient(circle, var(--slice) 55%, var(--slice-ring) 100%);
  }
  .contact {
    position: absolute;
    display: flex;
    align-items: center;
    gap: 5px;
    font-family: "Roboto Slab", serif;
    font-weight: 500;
    font-size: 12.5px;
    color: var(--cream);
    white-space: nowrap;
  }
  .contact--web { left: 36px; top: 260px; }
  .contact--phone { left: 800px; top: 268px; }
  .contact svg { width: 12px; height: 12px; }
</style>
</head>
<body>
  <section class="billboard" aria-label="The Driftmill billboard">
    <div class="food-frame food-frame--ribs" role="img" aria-label="Photo of smoked barbecue ribs over a grill"></div>
    <div class="food-frame food-frame--wrap" role="img" aria-label="Photo of a grilled wrap with salad and tomato"></div>

    <div class="activity-slice" style="left:248px;top:41px" role="img" aria-label="Wood slice with lodge cabin illustration"></div>
    <div class="activity-slice" style="left:357px;top:41px" role="img" aria-label="Wood slice with off road rider illustration"></div>
    <div class="activity-slice" style="left:302px;top:85px" role="img" aria-label="Wood slice with water skier illustration"></div>
    <div class="activity-slice" style="left:645px;top:41px" role="img" aria-label="Wood slice with tent illustration"></div>
    <div class="activity-slice" style="left:706px;top:85px" role="img" aria-label="Wood slice with angler illustration"></div>
    <div class="activity-slice" style="left:766px;top:41px" role="img" aria-label="Wood slice with hunter illustration"></div>

    <div class="brand brand__the">THE</div>
    <div class="brand brand__name">DRIFTMILL</div>
    <div class="brand brand__place">MARROWIND LAKE &amp; DAM</div>

    <h1 class="tagline">NEED A BREAK</h1>

    <ul class="activities activities--left">
      <li><span class="bullet" role="img" aria-label="Lodging icon"></span>LODGING</li>
      <li><span class="bullet" role="img" aria-label="Water skiing icon"></span>WATER SKIING</li>
      <li><span class="bullet" role="img" aria-label="Off road icon"></span>OFF ROAD ADVENTURE</li>
    </ul>
    <ul class="activities activities--right">
      <li><span class="bullet" role="img" aria-label="Camping icon"></span>CAMPING</li>
      <li><span class="bullet" role="img" aria-label="Fishing icon"></span>FISHING</li>
      <li><span class="bullet" role="img" aria-label="Hunting icon"></span>HUNTING</li>
    </ul>

    <div class="contact contact--web">
      <svg viewBox="0 0 12 12" fill="none" stroke="currentColor" stroke-width="1"><circle cx="6" cy="6" r="5"/><ellipse cx="6" cy="6" rx="2.2" ry="5"/><line x1="1" y1="6" x2="11" y2="6"/></svg>
      www.marrowinddriftmill.example
    </div>
    <div class="contact contact--phone">
      <svg viewBox="0 0 12 12" fill="currentColor"><path d="M2.5 1 L4.5 1 L5.3 3.4 L4 4.4 C4.7 5.9 6 7.2 7.6 8 L8.6 6.7 L11 7.5 L11 9.5 C11 10.3 10.3 11 9.5 11 C5 11 1 7 1 2.5 C1 1.7 1.7 1 2.5 1 Z"/></svg>
      (555) 014-2290
    </div>
  </section>
</body>
</html>
```